Your new Home.

below is a lot of info so you can read and understand what I do I think it's important for the creator to know as much as possible so you can creatively decide what would work in a flyer. I want it to be edgy, modern, or very aggressive. I am very loud and proud we don't want to be like everyone else. Our slogan Is "Where Craftsmen Come to Reach the Summit" as every one in my business calls themselves professionals and being a master to me means the best at what you do. which we are. my company colors are Gold Maroon Black and grey and whit. I do like having lightning strikes and hail incorperated. We Do Have Promotions and coupons and referals we pay out on. below this is a bunch of info to understand what I do. I need a flyer that is informative about my company. That informs customers what we want to do. We are a company with over 30 years combined experience Myself 13 yrs experience. We are a Storm Damage Specialist Restoration General Contractor Company. We provide a service the helps insure homeowners not only can we provide the correct perferred method of repairs according to today's industry standards rules and regulations. but we know what is your responsibility as a homeowner, and what the responsibility of your insurer is according to The governing municipalities not only by the city and state, but according to States Insurance Departments That govern what Insurance carriers must do. We don't let big conglomerate companies profiting off thousands of homeowners constantly paying in with their raising premiums each year. We use the Guidelines set by the insurance commissioners office to make sure that carriers are approving and paying for more than just minimums. Carriers constantly state to homeowners and contractors that their company policies don't allow things especially when it comes to paying for full roof replacements, replacing all your siding on the entire home if its discontinued. Or replacing all gutters ect. Carriers constantly are coming in only approving and paying for minor repairs And doing partial roof replacements, patching in siding replacing 1 and 2 peices here and their sections of fascia and gutters ect. we are tired of Carriers using their tactics of Denying claims, defering responsibility, defending them self's . Who's left to defend the homeowners? Who's knows the right questions to ask, and in what order and when to ask them. We Do. That's because for over a decade We have perfected the process of Working with hundred of different carriers. By already having major success on over a couple thousand Storm Damage claims . in more than a decade. Every last one of the claims we have worked on. Our goal was to maximize each claim to complete repairs restoring homeowners damaged properties to their original condition as they were prior to their loss. We can't get carriers to do anything they are not obligated to do. We have have to document and and present any and all damages we find. Then present it in a way to a carrier to where it can't be denied stating it doesn't meet certan criteria's, or deferred that its not storm damage that it was caused by a non covered peril, or defend that they are their to take care of you, and we are just trying to make money off of them regardless of actual responsibility. We can navigate through this process where we are the ones taking all the risks and doing all the leg work. Our Time is very valuable. We can only be as effective as our customers allow. Meaning A lot of times carriers will try to divide and conquer. Meaning they want to cause doubt in our abilities, or paint a pictured of alternative Motives That aren't in your best intrest. Carriers know their contracts are with the insured not the Contractors . That they don't have to answer to us
That's why its very important to us to set the tone early on. We are here to make money by performing excellent work restoring your property from storm damage. Ask your self , if we sign homeowners up for us to be the Contractor of choice to repair all approved works, and we only make money off of works completed than wouldn't we want to get you as much work approved for us to do. Leaving the homeowner and the contractor us having the same goal, however carriers dont want that because they are the ones having to pay for it back. They don't want to pay out huge portions they have accumulated from all your yearly premiums. All our works have to be approved by the carriers no carrier is going to pay thousands to their policy holders unless they have to. You are kidding yourself if you don't think they aren't saving millions by not paying out when they are legally bond to. You entered a bi lateral contract with them that you would give them x amount of dollars for a service they would provide if certain listed perils occurred while your insurance was binded / in affect. We know what works and what doesn't. In the end we also don't set the prices we use a 3rd party system that all the carriers use That is a automated computer system that populates the current fair market value of all materials amd labors. Know as the Replacement Cost Value. So if we don't make the rule, or set the prices, and we do all our works upfront with no down payment. Theirs no way a carrier can when a argument that we are doing anything other than working for you to create as much work for us that results in your property Being restored to its original condition at the same time it is restoring thousands of dollars of value back into your. home. Leaving you most prized financial investment protected. Our goals are t ok perform the best quality workmanship and keeping homeowners out of pocket cost to not exceed their set deductibles. If your cost is the same regardless you know when you file a claim you want everything that would be related to storm damaged documented and restored and paid for, and that's what we want because that's what we do for a living, and we want to be the best at it.

explaining the proccess.

We schedual a free no obligation gable crest property damage assesment/ inspection, what that intales is A roof inspection of all roof surfaces on property and a exterior inspection f all structures on the property Dwelling Detacjed Garages Barns, Shops, Well Houses and more. And finally interior inspections as well. Looking for water damage to ceilings and walls and floors.

Once we have photo documented all the damages notated during inspection, a gable crest will then sit down and go over all of them and show you pictures we took of those damages and explain why they we believe they should be paid for by your carrier as a covered peril on you homeowners policy. All with you only paying a
deductible that you chose when you started the policy. We will then use a storm Damage app to populate your best storm Date of Loss That best helps your scenario to get all damages paid for. once we have shown you the damages and explained them to you. we will give you a contingency contract that is based off of us getting your insurance company you approve and pay for them. if we can't get your project approved you don't owe us a dime for all that time we spent inspecting documenting and calling in your claim and meeting your insurance scheduled adjuster. As this is how we make a living is winding homeowners with storm related damage. so once you have decided to see what we can do for you we file your claim with you. Then the adjuster assigned will reach out to you usually within 1 to 10 business day most likely within the 1st 72 business hours. They will schedule a time to come do a inspection, which we ask you to contact us and share that information as this us a very crucial part to getting the right things documented to that adjuster with statements that would would contribute to the adjuster having to approve the documented damages t ok be restored Once the adjuster complete the inspection, he submits his estimate written on a computer system that we also use meaning neither of us set the price we are only entering apple for apples aka same like kind and value to be removed and replaced. price is bases off of you zipcode and month where and when the works were privided/ incurred . Leaving you the homeowner only responsible for your deductible. Was you receive your estimate we will go over all approves line items with you and schedule them with you to meat you time line of what you have going on in your life. we can cater to all needs. We are financially set to do the works as fast as you would like or hold off until a certain time. That doing said through this entire process we do not request any down payments amd will be able to take the financial risks of completing the works 1st so you are never in a position to where yo iij have paid any moneys wiring about what the work will look like or when it will get done. Once we have finished all approved scope of works. We send off to them the final invoice stating all works have been completed and they release the rest of the funds allowed for those works. we are a 1 stop shop that will handle a those types of repairs. From roofing siding fascia soffit aluminum wraps garage doors drywall repair and painting amd more.

Target Market(s)

Home Owners, Useually 25 years old at least to 80 year olds. Most will be 30-50

Industry/Entity Type

Construction

Colors

Designer to choose colors to be used in the design.

Requirements
Must have
• My Company Name, My Logo that you can find On my Chatter web or web site fd- Gable Crest Builders Inc. www.gablecrestbuilding.example
• My Slogan
• Where Craftsmen Reach the Summit
• Contact info phone (555)382-6047
Nice to have
• Hail, and wind images Beautiful homes, disasters. Lightning striking hail falling SEVERE wind. I LOVE COMEDY. so any thing that is catchy or funny. Like Not a Shingle Mistake. as are number 1 thing we do is R&R Roofing
Should not have
• My Name,

```html
<!DOCTYPE html>
<html lang="en">
<head>
<meta charset="utf-8">
<title>Gable Crest Builders Inc. – Storm Damage Restoration</title>
<link href="https://fonts.googleapis.com/css2?family=Arimo:wght@400&family=Cormorant+SC:wght@500;600&display=swap" rel="stylesheet">
<style>
  :root{
    --maroon:#7a1230;
    --maroon-deep:#5c0d24;
    --gold:#d4b866;
    --panel:rgba(38,36,40,0.93);
    --white:#ffffff;
    --ink:#2b2530;
    --sky-top:#aebde4;
    --sky-mid:#b7abd0;
    --dusk:#6e5870;
  }
  *{margin:0;padding:0;box-sizing:border-box}
  html,body{width:1200px;height:848px;overflow:hidden}
  body{font-family:"Arimo",Arial,sans-serif;position:relative;background:#fff}
  .flyer{position:absolute;inset:0;overflow:hidden}
  .backdrop{position:absolute;inset:0;
    background:
      radial-gradient(ellipse 520px 260px at 650px 520px, rgba(70,66,98,.55), transparent 70%),
      linear-gradient(180deg,var(--sky-top) 0%,var(--sky-mid) 45%,#a78eaa 62%,var(--dusk) 100%);}
  .dots{position:absolute;left:8px;top:8px}
  .line{display:block;white-space:nowrap}
  .panel{position:absolute;background:var(--panel);color:var(--white);font-size:17px;line-height:20.5px}
  .panel-left{left:33px;top:45px;width:329px;height:573px;padding:22px 0 0 22px}
  .panel-left .gap{height:20.5px}
  .panel-center{left:435px;top:176px;width:328px;height:672px;padding:14px 0 0 18px}
  .panel-center .second{margin-top:6px}
  .intro-blob{position:absolute;left:432px;top:10px;width:328px;height:161px;background:var(--gold);
    border-radius:28px 12px 150px 0/28px 12px 110px 0;padding:9px 0 0 13px;
    color:var(--maroon);font-size:17px;line-height:20.4px}
  .stripes{position:absolute;left:800px;top:0}
  .brand{position:absolute;left:845px;top:178px;width:300px;display:flex;
    align-items:center;justify-content:center;gap:10px}
  .brand-mark{width:18px;height:18px;border-radius:50%;background:var(--maroon);flex:none}
  .brand-name{font-family:"Cormorant SC",Georgia,serif;font-weight:600;font-size:24px;color:var(--maroon);line-height:1;white-space:nowrap}
  .slogan{position:absolute;left:840px;top:262px;width:330px;text-align:center;
    font-family:"Cormorant SC",Georgia,serif;font-weight:500;font-size:31px;line-height:34px;color:var(--maroon)}
  .tagline{position:absolute;left:830px;top:388px;width:330px;text-align:center;font-size:18.5px;line-height:24px;color:var(--ink)}
  .photo{position:absolute;left:0;top:0}
</style>
</head>
<body>
<main class="flyer">
  <div class="backdrop" role="img" aria-label="Photo of a large grey suburban house at dusk under a lavender sky"></div>

  <svg class="dots" width="160" height="160" viewBox="0 0 160 160" aria-hidden="true">
    <g fill="var(--maroon)">
      <circle cx="4" cy="4" r="3"/><circle cx="34" cy="4" r="3"/><circle cx="63" cy="4" r="3"/><circle cx="93" cy="4" r="3"/><circle cx="122" cy="4" r="3"/><circle cx="151" cy="4" r="3"/>
      <circle cx="4" cy="34" r="3"/><circle cx="34" cy="34" r="3"/><circle cx="63" cy="34" r="3"/><circle cx="93" cy="34" r="3"/><circle cx="122" cy="34" r="3"/><circle cx="151" cy="34" r="3"/>
      <circle cx="4" cy="63" r="3"/><circle cx="4" cy="94" r="3"/><circle cx="4" cy="124" r="3"/><circle cx="4" cy="153" r="3"/>
    </g>
  </svg>

  <svg class="stripes" width="400" height="175" viewBox="0 0 400 175" aria-hidden="true">
    <g fill="var(--maroon)">
      <rect x="0" y="0" width="194" height="6"/><rect x="199" y="0" width="201" height="6"/>
      <rect x="0" y="27" width="179" height="6"/><rect x="212" y="27" width="188" height="6"/>
      <rect x="0" y="54" width="146" height="6"/><rect x="245" y="54" width="155" height="6"/>
      <rect x="0" y="82" width="113" height="6"/><rect x="278" y="82" width="122" height="6"/>
      <rect x="0" y="109" width="80" height="6"/><rect x="312" y="109" width="88" height="6"/>
      <rect x="0" y="137" width="47" height="6"/><rect x="345" y="137" width="55" height="6"/>
      <rect x="0" y="164" width="14" height="6"/><rect x="378" y="164" width="22" height="6"/>
    </g>
  </svg>

  <div class="brand"><span class="brand-mark"></span><span class="brand-name">Gable Crest Builders Inc.</span></div>

  <h1 class="slogan">“Where Craftsmen Come to Reach the Summit”</h1>

  <p class="tagline">Don’t&nbsp; have any idea how to get best of your inscurance<br>we have got you covered</p>

  <section class="panel panel-left">
    <span class="line">We are here to make money by</span>
    <span class="line">performing excellent work restoring</span>
    <span class="line">your property from storm damage.</span>
    <span class="line gap"></span>
    <span class="line">Ask your self , if we sign homeowners</span>
    <span class="line">up for us to be the Contractor of</span>
    <span class="line">choice to repair all approved works,</span>
    <span class="line">and we only make money off of works</span>
    <span class="line">completed than wouldn't we want to</span>
    <span class="line">get you as much work approved for us</span>
    <span class="line">to do. Leaving the homeowner and the</span>
    <span class="line">contractor us having the same goal,</span>
    <span class="line">however carriers dont want that</span>
    <span class="line">because they are the ones having to</span>
    <span class="line">pay for it back. They don't want to pay</span>
    <span class="line">out huge portions they have</span>
    <span class="line">accumulated from all your yearly</span>
    <span class="line">premiums.</span>
    <span class="line gap"></span>
    <span class="line">All our works have to be approved by</span>
    <span class="line">the carriers no carrier is going to pay</span>
    <span class="line">thousands to their policy holders</span>
    <span class="line">unless they have to. You are kidding</span>
    <span class="line">yourself if you don't think they aren't</span>
    <span class="line">saving millions by not paying out</span>
    <span class="line">when they are legally bond to.</span>
  </section>

  <svg class="photo" width="1200" height="848" viewBox="0 0 1200 848">
    <defs>
      <linearGradient id="hail-street" x1="0" y1="0" x2="0" y2="1">
        <stop offset="0" stop-color="#5d6470"/><stop offset=".45" stop-color="#3e4448"/><stop offset="1" stop-color="#8a8f8e"/>
      </linearGradient>
    </defs>
    <path d="M0,628 C120,606 320,606 428,620 C446,690 452,780 455,848 L0,848 Z" fill="var(--maroon-deep)"/>
    <path d="M0,636 C120,616 316,616 420,628 C436,700 442,780 445,848 L0,848 Z" fill="url(#hail-street)" role="img" aria-label="Photo of a city intersection covered in hail during a storm"/>
  </svg>

  <aside class="intro-blob">
    <span class="line">We provide a service the helps insure</span>
    <span class="line">homeowners not only can we provide</span>
    <span class="line">the correct perferreWe are a company</span>
    <span class="line">with over 30 years.</span>
    <span class="line">We are a Storm Damage Specialist</span>
    <span class="line">Restoration General Contractor</span>
    <span class="line">Company.</span>
  </aside>

  <section class="panel panel-center">
    <span class="line">We provide a service the helps insure</span>
    <span class="line">homeowners not only can we provide</span>
    <span class="line">the correct perferred method of</span>
    <span class="line">repairs according to today's industry</span>
    <span class="line">standards rules and regulations.</span>
    <span class="line">But we know what is your</span>
    <span class="line">responsibility as a homeowner, and</span>
    <span class="line">what the responsibility of your insurer</span>
    <span class="line">is according to The governing</span>
    <span class="line">municipalities not only by the city and</span>
    <span class="line">state, but according to States</span>
    <span class="line">Insurance Departments That govern</span>
    <span class="line">what Insurance carriers must do.</span>
    <span class="line second">We don't let big conglomerate</span>
    <span class="line">companies profiting off thousands of</span>
    <span class="line">homeowners constantly paying in with</span>
    <span class="line">their raising premiums each year. We</span>
    <span class="line">use the Guidelines set by the</span>
    <span class="line">insurance commissioners office</span>
    <span class="line">to make sure that carriers are</span>
    <span class="line">approving and paying for</span>
    <span class="line" style="padding-left:4px">more than just minimums.</span>
    <span class="line" style="padding-left:12px">Carriers constantly state</span>
    <span class="line" style="padding-left:16px">to homeowners and</span>
    <span class="line" style="padding-left:18px">contractors that their</span>
    <span class="line" style="padding-left:16px">company policies don't</span>
    <span class="line" style="padding-left:11px">allow things especially</span>
    <span class="line" style="padding-left:4px">when it comes to</span>
    <span class="line">paying for full roof</span>
    <span class="line">replacements.</span>
  </section>

  <svg class="photo" width="1200" height="848" viewBox="0 0 1200 848">
    <defs>
      <linearGradient id="storm-house" x1="0" y1="0" x2="0" y2="1">
        <stop offset="0" stop-color="#6a2f55"/><stop offset=".45" stop-color="#8a4a78"/><stop offset=".75" stop-color="#5a5460"/><stop offset="1" stop-color="#3f4a44"/>
      </linearGradient>
    </defs>
    <path d="M612,848 C632,715 684,592 762,522 C804,486 852,476 904,474 L1200,474 L1200,848 Z" fill="var(--maroon-deep)"/>
    <path d="M634,848 C652,722 702,604 776,536 C816,500 862,490 912,488 L1200,488 L1200,848 Z" fill="url(#storm-house)" role="img" aria-label="Photo of a lit two-storey house with garage under a purple sky with lightning strikes"/>
  </svg>
</main>
</body>
</html>
```